Anzeigengestaltung für einen einen ambulanten Pflegedienst
Zielgruppe
Insgesamt möchte ich gern drei Anzeigen für das Internet gestalten haben. Ich betreibe einen ambulanten Pflegedienst. Die erste Anzeige soll dazu dienen Kunden anzusprechen, die einen Unterstützungsbedarf und / oder einen Beratungsbedarf haben. Die zweite Anzeige soll dazu dienen neues Personal anzuwerben. Die dritte Anzeige soll speziell potenzielle Azubis ansprechen. Die Anzeigen sind gedacht für Chatterwall und Pixelora hauptsächlich. In den Druck sollte es schon 10cm x 8cm sein. Es wäre super wenn vielleicht auch eine Art Aufruf an ehrenamtliche Mitarbeiter erfolgt.
Aufgabenstellung
Die Anzeigen sollen den Stil der Homepage beibehalten. Freundlich, frisch und agil wirken. Alle sollten emotional ansprechend sein und gerade der für zukünftige Mitarbeiter sollte deutlich ein gutes Betriebsklima vermitteln. Als Datei habe ich einige Bilder, die bereits für die Homepage oder Flyer verwendet wurden hochgeladen. des Weiteren habe ich die einzelnen Seiten des Flyers hochgeladen.

```html
<!DOCTYPE html>
<html lang="de">
<head>
<meta charset="utf-8">
<title>Team Lorvana – Der Mensch im Mittelpunkt</title>
<link href="https://fonts.googleapis.com/css2?family=Playfair+Display:wght@400&family=Quicksand:wght@500;700&display=swap" rel="stylesheet">
<style>
  :root{
    --teal:#4aafab;
    --green:#7cb03a;
    --ink:#5f5f5f;
    --band:#e0f0f9;
    --ring:#d8ebf6;
    --white:#ffffff;
  }
  *{margin:0;padding:0;box-sizing:border-box}
  html,body{width:1200px;height:960px;overflow:hidden;background:var(--white)}
  .ad{position:relative;width:1200px;height:960px;overflow:hidden;background:var(--white);font-family:'Quicksand',sans-serif;color:var(--ink)}
  .photo{position:absolute;left:545px;top:-596px;width:1136px;height:1136px;border-radius:50%;
    background:radial-gradient(circle at 62% 78%, #c9a08c 0%, #b58a76 10%, #d9dcdf 24%, #eceef1 45%, #f4f5f7 70%);}
  .accent-arcs{position:absolute;left:0;top:0}
  .kicker{position:absolute;left:60px;top:62px;font-family:'Playfair Display',serif;font-size:38px;font-weight:400;color:var(--ink);letter-spacing:.2px}
  .headline{position:absolute;left:60px;top:125px;font-weight:700;font-size:60px;line-height:63px;color:var(--teal);letter-spacing:.3px}
  .headline .warm{color:var(--green)}
  .rule{position:absolute;left:60px;top:345px;width:303px;height:5px;background:var(--green)}
  .lead{position:absolute;left:60px;top:385px;font-size:33px;font-weight:500;line-height:43px;color:var(--ink)}
  .services{position:absolute;list-style:none;font-size:33px;font-weight:500;color:var(--ink)}
  .services li{position:relative;padding-left:29px}
  .services li::before{content:"+";position:absolute;left:0;color:var(--green)}
  .services.left{left:60px;top:588px}
  .services.left li{height:59px}
  .services.right{left:612px;top:588px}
  .services.right li{line-height:47px;margin-bottom:12px}
  .band{position:absolute;left:0;top:810px;width:1200px;height:150px;background:var(--band)}
  .pill{position:absolute;top:854px;height:62px;border-radius:31px;display:flex;align-items:center;justify-content:center;font-family:'Playfair Display',serif;font-size:33px;color:var(--white)}
  .pill.claim{left:35px;width:350px;background:var(--green)}
  .pill.web{left:417px;width:429px;background:var(--teal)}
  .brand{position:absolute;left:958px;top:718px;width:212px;height:212px;border-radius:50%;background:var(--white);border:3px solid var(--ring);display:flex;flex-direction:column;align-items:center;justify-content:center;gap:14px}
  .brand .dot{width:46px;height:46px;border-radius:50%;background:var(--teal)}
  .brand .name{font-weight:700;font-size:22px;color:var(--ink);letter-spacing:.5px}
</style>
</head>
<body>
<div class="ad">
  <div class="photo" role="img" aria-label="Foto: Pflegekraft legt ihre Hand auf die Hand einer älteren Person am Griff eines Rollators"></div>

  <svg class="accent-arcs" width="1200" height="960" viewBox="0 0 1200 960" aria-hidden="true">
    <path d="M670 497 C670 440 705 415 760 411 C790 409 815 413 827 423" fill="none" stroke="var(--teal)" stroke-width="6" stroke-linecap="round"/>
    <path d="M698 557 C700 510 712 470 724 459 C745 443 800 445 846 463" fill="none" stroke="var(--green)" stroke-width="6" stroke-linecap="round"/>
  </svg>

  <p class="kicker">Der Mensch im Mittelpunkt</p>
  <h1 class="headline">Für uns ist Pflege<br>eine <span class="warm">Herzens-</span><br><span class="warm">angelegenheit!</span></h1>
  <div class="rule"></div>
  <p class="lead">Sie das Gefühl haben ein:e<br>Angehörige:r braucht Hilfe bzw.<br>Unterstützung? Wir sind für Sie da!</p>

  <ul class="services left">
    <li>Grund- und Behandlungspflege</li>
    <li>Beratungseinsatz</li>
    <li>Hauswirtschaftliche Leistungen</li>
  </ul>
  <ul class="services right">
    <li>Entlastungs- und<br>Betreuungsangebote</li>
    <li>Verhinderungspflege</li>
  </ul>

  <div class="band"></div>
  <div class="pill claim">Wir sind für Sie da!</div>
  <div class="pill web">www.lorvana-pflege.de</div>

  <div class="brand">
    <span class="dot"></span>
    <span class="name">TEAM LORVANA</span>
  </div>
</div>
</body>
</html>
```